Valdora Business Card Design - Professional Flexible and forward thinking. Clean and Easy to follow

Management Consulting Company. I focus on business development and concept and operational review. I need a progressive, simple and professional layout design for the business cards, letterhead and envelops
Professional Flexible and forward thinking. Clean and Easy to follow
Mature Business persons and professionals and Corporations

Target Market(s)

Mature Business persons and professionals and Corporations - Government org.

Industry/Entity Type

Consulting

Contact Information for Business Card

Requirements
Must have
• Marcus Valdora
• President
• Phone - 516.382.6047
• email - Mvaldora@valdorapartners.com
• Skype - Marc.valdora
• 7215 Pellham Avenue
• Suite A
• Larchmere, N.Y. 11594
• USA
Nice to have
• www.valdorapartners.com
Should not have
• N/A

```html
<!DOCTYPE html>
<html lang="en">
<head>
<meta charset="utf-8">
<title>Valdora Partners – Business Card</title>
<link href="https://fonts.googleapis.com/css2?family=Questrial&display=swap" rel="stylesheet">
<style>
  :root {
    --stage: #4a4541;
    --card-light: #f4f4f2;
    --card-dark: #2b2a29;
    --ink: #3a3a3a;
    --ink-soft: #e2e2e2;
    --accent: #e5512b;
  }
  * { margin: 0; padding: 0; box-sizing: border-box; }
  html, body { width: 1200px; height: 727px; overflow: hidden; }
  body {
    background: var(--stage);
    font-family: "Questrial", "Century Gothic", sans-serif;
    position: relative;
  }
  .card {
    position: absolute;
    top: 209px;
    width: 540px;
    height: 309px;
    border-radius: 3px;
    box-shadow: 0 10px 30px rgba(0,0,0,.35);
  }
  .card-front { left: 40px; background: var(--card-light); color: var(--ink); }
  .card-back { left: 620px; background: var(--card-dark); color: var(--ink-soft); }

  .brand { display: flex; align-items: center; gap: 10px; position: absolute; }
  .brand-mark { background: var(--accent); border-radius: 3px; }
  .brand-name {
    letter-spacing: .12em;
    text-transform: uppercase;
    line-height: 1;
    white-space: nowrap;
  }
  .card-front .brand { left: 30px; top: 30px; }
  .card-front .brand-mark { width: 30px; height: 30px; }
  .card-front .brand-name { font-size: 19px; color: var(--accent); }

  .person { position: absolute; left: 36px; top: 132px; }
  .person-name { font-size: 22px; color: var(--ink); }
  .person-title { font-size: 13px; color: var(--accent); margin-top: 2px; }

  .contact { position: absolute; left: 258px; top: 150px; list-style: none; font-size: 13px; }
  .contact li { display: flex; align-items: flex-start; gap: 8px; line-height: 1.35; margin-bottom: 4px; white-space: nowrap; }
  .contact svg { width: 13px; height: 13px; flex: none; margin-top: 2px; fill: var(--accent); }

  .card-back .brand { left: 50%; top: 108px; transform: translateX(-50%); gap: 14px; }
  .card-back .brand-mark { width: 44px; height: 44px; }
  .card-back .brand-name { font-size: 27px; color: var(--ink-soft); }
  .website {
    position: absolute; left: 0; right: 0; top: 206px;
    text-align: center; font-size: 17px; letter-spacing: .02em;
  }
  .website .accent { color: var(--accent); }
</style>
</head>
<body>
  <section class="card card-front">
    <div class="brand">
      <span class="brand-mark"></span>
      <span class="brand-name">Valdora Partners</span>
    </div>
    <div class="person">
      <p class="person-name">Marcus Valdora</p>
      <p class="person-title">President</p>
    </div>
    <ul class="contact">
      <li>
        <svg viewBox="0 0 16 16" aria-hidden="true"><path d="M2 5c0-2 2-3 6-3s6 1 6 3v1h-3V5H5v1H2zM4 7h8l2 6H2z"/></svg>
        <span>516.382.6047</span>
      </li>
      <li>
        <svg viewBox="0 0 16 16" aria-hidden="true"><path d="M1 3h14v10H1zM2 4l6 5 6-5v-.2H2z" fill-rule="evenodd"/></svg>
        <span>Mvaldora@valdorapartners.com</span>
      </li>
      <li>
        <svg viewBox="0 0 16 16" aria-hidden="true"><circle cx="8" cy="8" r="7"/></svg>
        <span>Skype - Marc.valdora</span>
      </li>
      <li>
        <svg viewBox="0 0 16 16" aria-hidden="true"><path d="M8 1a5 5 0 0 1 5 5c0 4-5 9-5 9S3 10 3 6a5 5 0 0 1 5-5zm0 3a2 2 0 1 0 0 4 2 2 0 0 0 0-4z" fill-rule="evenodd"/></svg>
        <span>7215 Pellham Avenue, Suite A<br>Larchmere, N.Y. 11594, USA</span>
      </li>
    </ul>
  </section>

  <section class="card card-back">
    <div class="brand">
      <span class="brand-mark"></span>
      <span class="brand-name">Valdora Partners</span>
    </div>
    <p class="website"><span class="accent">www.</span>valdorapartners<span class="accent">.com</span></p>
  </section>
</body>
</html>
```